Theater Production Company in Las Vegas

Needing a business card for a theater production company in Las Vegas. We are a full service theatrical production company specializing in Las Vegas entertainment, national
touring shows, and one-off events. From gorilla marketing teams to large scale productions... we do it,and better than anyone.

We like the feel of something hand made and organic.The final design should be creative and communicate that we specialize in theater and special events. We would like to have a design with a front and back.

Hi All,

I want to elaborate on the style of the design that we are hoping for. We are a theater production company in Las Vegas, so the competition is fierce and having a clever business card is incredibly important. 

I am attached a few concepts of a "feel" that would be nice to have conveyed in our card. We love the "worn and vintage" feel that is often seen in antique circus posters. Traditionally, the circus posters are clustered and full of copy - I want a more simplified version of that. Not so cluttered, but with that worn feel. Perhaps even having the card printed on recycled paper to give that textured feel to the visual. 

Example 1 - has a fun worn look, with stars. Some version of this for the back of the card would be fun.
Example 2 - Same things, cool worn feel. Perhaps a small star at the center of the swirl and a little softer on the "grunge".
Example 3 - Has the circus ornament but the colors are nice, not overpowering and again, has that worn feel.
Example 4 - This design isn't as "tight" and cluttered. Has some room to breathe.
Example 5 - I am really liking the look of the this and the above, especially for the back of the card. 

But just to reiterate, the front and face of the card needs to be clear and easy to read. 

Hi Designers, 

I have posted an update so you can have a clearer understanding of what we are needing. I have also increased the funding.

Thank you in advance for your help.

Bridget

Industry/Entity Type

Marketing

Requirements
Must have
• We want to assign creative license. We are creative and hate to be limited by restrictions. Have fun!

The attached files are our logo. One of the files is a business card design that I love. Just a sample of our taste.
Nice to have
• We would like to incorporate: Merchants of Marvelous Shows
as our tagline. I like a vintage, worn feel to the look of designs. Just the word "purveyor" sounds vintage.

```html
<!DOCTYPE html>
<html lang="en">
<head>
<meta charset="utf-8">
<title>Velvet Lantern Productions – Business Card</title>
<link rel="stylesheet" href="https://fonts.googleapis.com/css2?family=Roboto+Slab:wght@800&family=Libre+Baskerville:wght@400;700&family=Montserrat:wght@500&family=Pinyon+Script&display=swap">
<style>
  :root {
    --stage: #e4e3e0;
    --paper-light: #fbf4d6;
    --paper-mid: #f3e2a6;
    --paper-warm: #ecd38e;
    --ink: #1c1a17;
    --circus-red: #b8392a;
    --circus-blue: #1f6d8f;
    --cream: #f5edd4;
    --gold-light: #f1dfa8;
    --gold-dark: #b8955a;
    --tagline: #f7e7b8;
  }
  * { box-sizing: border-box; margin: 0; padding: 0; }
  html, body {
    width: 1200px; height: 795px; overflow: hidden;
    background: var(--stage);
  }
  .canvas { position: relative; width: 1200px; height: 795px; }

  .card { position: absolute; box-shadow: 0 6px 14px rgba(0,0,0,.28); overflow: hidden; }

  /* Front */
  .card-front { left: 56px; top: 311px; width: 656px; height: 371px; }
  .card-front svg { display: block; }

  /* Back */
  .card-back {
    left: 772px; top: 84px; width: 372px; height: 655px;
    background: radial-gradient(ellipse at 75% 20%, var(--paper-light) 0%, var(--paper-mid) 55%, var(--paper-warm) 100%);
    color: var(--ink);
  }
  .brand {
    position: absolute; top: 36px; left: 0; width: 100%;
    text-align: center; font-family: "Libre Baskerville", serif; color: var(--ink);
  }
  .brand-dot {
    display: block; width: 34px; height: 34px; margin: 0 auto 14px;
    border-radius: 50%; background: var(--ink);
  }
  .brand-name { font-size: 30px; line-height: 1.15; font-weight: 400; }
  .brand-sub { font-size: 30px; font-weight: 400; line-height: 1.15; }

  .person {
    position: absolute; top: 226px; left: 0; width: 100%; text-align: center;
    font-family: "Roboto Slab", serif; font-weight: 800; font-size: 24px; letter-spacing: .5px;
  }
  .rule {
    position: absolute; left: 14px; right: 14px; height: 0;
    border-top: 2px dotted var(--ink);
  }
  .rule-1 { top: 283px; } .rule-2 { top: 425px; } .rule-3 { top: 537px; }

  .contacts { position: absolute; top: 292px; left: 32px; list-style: none; }
  .contacts li {
    display: flex; align-items: center; height: 31.5px;
    font-family: "Montserrat", sans-serif; font-size: 19px; font-weight: 500;
  }
  .contacts svg { width: 16px; height: 16px; margin-right: 14px; flex: none; }
  .contacts .sep { margin-right: 10px; }

  .address {
    position: absolute; top: 443px; left: 0; width: 100%; text-align: center;
    font-family: "Libre Baskerville", serif; font-size: 17px; line-height: 29px;
    font-style: normal;
  }
  .address strong { font-weight: 700; }

  .swoosh { position: absolute; left: 0; bottom: 0; width: 372px; height: 96px; }
  .tagline {
    position: absolute; left: 0; bottom: 6px; width: 100%; text-align: center;
    font-family: "Pinyon Script", cursive; font-size: 27px; color: var(--tagline);
    white-space: nowrap;
  }
</style>
</head>
<body>
<main class="canvas">

  <section class="card card-front" aria-label="Card front">
    <svg width="656" height="371" viewBox="0 0 656 371">
      <defs>
        <radialGradient id="burst" cx="50%" cy="52%" r="70%">
          <stop offset="0" stop-color="#f4ead0"/>
          <stop offset=".55" stop-color="#e7d6b6"/>
          <stop offset=".8" stop-color="#c9877a"/>
          <stop offset="1" stop-color="#6c8fa6"/>
        </radialGradient>
        <linearGradient id="ribbon" x1="0" x2="1">
          <stop offset="0" stop-color="var(--gold-dark)"/>
          <stop offset=".3" stop-color="var(--gold-light)"/>
          <stop offset=".7" stop-color="var(--gold-light)"/>
          <stop offset="1" stop-color="var(--gold-dark)"/>
        </linearGradient>
        <radialGradient id="plate" cx="50%" cy="45%" r="60%">
          <stop offset="0" stop-color="#fbf1c9"/>
          <stop offset="1" stop-color="#ecd79a"/>
        </radialGradient>
      </defs>
      <rect class="sunburst" width="656" height="371" fill="url(#burst)" role="img" aria-label="Worn red, white and blue circus sunburst with stars"/>
      <path class="ribbon" d="M36 165 L620 165 L646 300 L604 318 L50 318 L14 300 Z" fill="url(#ribbon)" role="img" aria-label="Curled gold ribbon banner"/>
      <ellipse class="oval-frame" cx="329" cy="193" rx="213" ry="110" fill="var(--circus-red)"/>
      <ellipse cx="329" cy="193" rx="203" ry="101" fill="var(--cream)"/>
      <ellipse cx="329" cy="193" rx="198" ry="96" fill="var(--circus-blue)"/>
      <ellipse cx="329" cy="193" rx="191" ry="89" fill="url(#plate)"/>
      <circle cx="329" cy="152" r="14" fill="var(--ink)"/>
      <text x="329" y="212" text-anchor="middle" font-family="Libre Baskerville, serif" font-size="38" fill="var(--ink)">Velvet Lantern</text>
    </svg>
  </section>

  <section class="card card-back" aria-label="Card back">
    <div class="brand">
      <span class="brand-dot"></span>
      <div class="brand-name">Velvet Lantern</div>
      <div class="brand-sub">Productions</div>
    </div>

    <h1 class="person">BRIDGET CALLOWAY</h1>
    <div class="rule rule-1"></div>

    <ul class="contacts">
      <li><svg viewBox="0 0 16 16"><rect x="4" y="1" width="8" height="14" rx="1.5" fill="var(--ink)"/><rect x="5.5" y="3" width="5" height="5" fill="var(--paper-light)"/></svg><span class="sep">:</span>702 555 0148</li>
      <li><svg viewBox="0 0 16 16"><rect x="1" y="4" width="14" height="11" rx="1.5" fill="var(--ink)"/><rect x="3" y="1" width="4" height="5" rx="1" fill="var(--ink)"/><rect x="9" y="6" width="4" height="3" fill="var(--paper-light)"/></svg><span class="sep">:</span>702 555 0193</li>
      <li><svg viewBox="0 0 16 16"><rect x="1" y="3" width="14" height="10" fill="var(--ink)"/><path d="M1.5 3.5 L8 9 L14.5 3.5" stroke="var(--paper-light)" stroke-width="1.3" fill="none"/></svg><span class="sep">:</span>bridget@velvetlantern.com</li>
      <li><svg viewBox="0 0 16 16" fill="none" stroke="var(--ink)" stroke-width="1.2"><circle cx="8" cy="8" r="6.5"/><ellipse cx="8" cy="8" rx="3" ry="6.5"/><path d="M1.5 8 H14.5 M2.5 4.8 H13.5 M2.5 11.2 H13.5"/></svg><span class="sep">:</span>www.velvetlantern.com</li>
    </ul>
    <div class="rule rule-2"></div>

    <address class="address">
      <strong>Velvet Lantern Productions</strong><br>
      3120 Canyon Mesa Drive<br>
      Las Vegas, NV 89134
    </address>
    <div class="rule rule-3"></div>

    <svg class="swoosh" viewBox="0 0 372 96" preserveAspectRatio="none">
      <path d="M0 0 C90 30 200 36 372 24 L372 96 L0 96 Z" fill="var(--circus-blue)"/>
      <path d="M0 16 C100 40 220 40 372 28 L372 96 L0 96 Z" fill="var(--paper-mid)"/>
      <path d="M0 24 C110 46 230 44 372 32 L372 96 L0 96 Z" fill="var(--circus-red)"/>
    </svg>
    <p class="tagline">Merchants of Marvelous Shows</p>
  </section>

</main>
</body>
</html>
```